dorwial business card design so that it looks better

need a new business card designed. use our website, dorwian.com for example. I attached an example of a previous card we had and liked. this is for law enforcement and we have attached a previous business card as an example. This site forces me to select color and font, ignore those as I picked stuff just to get this completed.

Target Market(s)

law enforcement, local government

Contact Information for Business Card

see the attached example and our website

Font styles to use
Serif

```html
<!DOCTYPE html>
<html lang="en">
<head>
<meta charset="utf-8">
<title>Dorwial Business Card</title>
<link rel="stylesheet" href="https://fonts.googleapis.com/css2?family=Roboto:wght@300;400;500;700&display=swap">
<style>
  :root {
    --backdrop: #4a4a4a;
    --card: #1c1c1c;
    --ink: #ffffff;
    --ink-soft: #d9d9d9;
    --rule: #bfbfbf;
    --wordmark: #d6d6d6;
  }
  * { margin: 0; padding: 0; box-sizing: border-box; }
  html, body {
    width: 963px;
    height: 1200px;
    overflow: hidden;
    background: var(--backdrop);
    font-family: "Roboto", Arial, sans-serif;
    color: var(--ink);
  }
  .canvas { position: relative; width: 963px; height: 1200px; }
  .card {
    position: absolute;
    left: 232px;
    width: 556px;
    height: 317px;
    background: var(--card);
  }
  .card--front { top: 221px; }
  .card--back { top: 636px; }

  .holder {
    position: absolute;
    right: calc(556px - 269px);
    top: 129px;
    text-align: right;
  }
  .holder__name { font-size: 22px; font-weight: 700; line-height: 1.2; letter-spacing: 0.1px; }
  .holder__title { font-size: 15px; font-weight: 500; color: var(--ink-soft); line-height: 1.2; }

  .divider {
    position: absolute;
    left: 286px;
    top: 135px;
    width: 1px;
    height: 49px;
    background: var(--rule);
  }

  .contacts {
    position: absolute;
    left: 302px;
    top: 131px;
    list-style: none;
  }
  .contacts li {
    display: flex;
    align-items: center;
    height: 19px;
    font-size: 14px;
    font-weight: 400;
  }
  .contacts svg { width: 13px; height: 13px; margin-right: 9px; fill: var(--ink); flex: none; }

  .address {
    position: absolute;
    left: 0;
    right: 0;
    top: 260px;
    display: flex;
    justify-content: center;
    align-items: center;
    font-size: 14px;
    padding-left: 10px;
  }
  .address svg { width: 12px; height: 16px; margin-right: 6px; fill: var(--ink); }

  .wordmark {
    position: absolute;
    left: 0;
    right: 0;
    top: 124px;
    text-align: center;
    font-size: 52px;
    font-weight: 300;
    letter-spacing: 8px;
    padding-left: 8px;
    line-height: 60px;
    color: var(--wordmark);
  }
</style>
</head>
<body>
<main class="canvas">
  <section class="card card--front" aria-label="Card front">
    <div class="holder">
      <p class="holder__name">Daniel Hartwell</p>
      <p class="holder__title">President</p>
    </div>
    <span class="divider"></span>
    <ul class="contacts">
      <li>
        <svg viewBox="0 0 24 24" aria-hidden="true"><path d="M6.6 10.8a15.2 15.2 0 0 0 6.6 6.6l2.2-2.2a1 1 0 0 1 1-.25 11.4 11.4 0 0 0 3.6.57 1 1 0 0 1 1 1V20a1 1 0 0 1-1 1A17 17 0 0 1 3 4a1 1 0 0 1 1-1h3.5a1 1 0 0 1 1 1c0 1.25.2 2.45.57 3.57a1 1 0 0 1-.25 1z"/></svg>
        555.014.2290
      </li>
      <li>
        <svg viewBox="0 0 24 24" aria-hidden="true"><path d="M2 5h20v14H2z M4 7v.4l8 5 8-5V7l-8 5z" fill-rule="evenodd"/></svg>
        info@dorwian.com
      </li>
      <li>
        <svg viewBox="0 0 24 24" aria-hidden="true"><path d="M12 2a10 10 0 1 0 0 20 10 10 0 0 0 0-20zm-1 17.9A8 8 0 0 1 4.1 11H7l4 4zm6.9-2.5A2 2 0 0 0 16 16h-1v-3a1 1 0 0 0-1-1H8v-2h2a1 1 0 0 0 1-1V7h2a2 2 0 0 0 2-2v-.4a8 8 0 0 1 2.9 12.8z"/></svg>
        www.dorwian.com
      </li>
    </ul>
    <p class="address">
      <svg viewBox="0 0 24 32" aria-hidden="true"><path d="M12 0a12 12 0 0 0-12 12c0 9 12 20 12 20s12-11 12-20A12 12 0 0 0 12 0zm0 17a5 5 0 1 1 0-10 5 5 0 0 1 0 10z"/></svg>
      4182 Larkspur Avenue, Fairview, TX 75069
    </p>
  </section>

  <section class="card card--back" aria-label="Card back">
    <p class="wordmark">DORWIAL</p>
  </section>
</main>
</body>
</html>
```